New florist business website design

Number 1 want is an easy to navigate & check out website
Needs to be beautiful and eye catching as well.
This is an online only business (no shop front)
Rustic and blush pinks, neutrals, woods, leaves
Customers need to be able to go onto my website, select something they want to buy but have the option to use a drop down box to change colours of the flowers, or add notes to make changes to the arrangement

Industry/Entity Type

Florist

Coding

Coded - Design and coding required

Number of Pages Required

5+ page

Colors
f9d9e8
fff2ec
fffefc

Requirements
Must have
• Drop down menu to take you to other pages for Arrangements, bouquets, everlasting arrangements, gifts, contact
Be able to purchase and “add to basket”
Checkout page
Nice to have
• Be able to add my own photos once I’ve taken new ones
Should not have
• Tacky images or clip art

```html
<!DOCTYPE html>
<html lang="en">
<head>
<meta charset="utf-8">
<title>Petal &amp; Pine — Florist</title>
<link href="https://fonts.googleapis.com/css2?family=Dancing+Script:wght@400;500&family=Poppins:wght@400;500;600&display=swap" rel="stylesheet">
<style>
:root{
  --blush:#f9d9e8;
  --cream:#fff2ec;
  --white:#fffefc;
  --pink:#f0609e;
  --pink-soft:#f7a8c9;
  --sand:#f6dccb;
  --ink:#1f1f1f;
  --muted:#6b6b6b;
  --footer-dark:#111;
}
*{box-sizing:border-box;margin:0;padding:0}
html,body{width:1200px;height:4853px;overflow:hidden}
body{position:relative;background:var(--white);font-family:"Poppins",sans-serif;color:var(--ink)}
.abs{position:absolute}
.script{font-family:"Dancing Script",cursive;font-weight:400}
a{color:inherit;text-decoration:none}

/* header */
.site-header{position:absolute;left:0;top:0;width:1200px;height:150px;background:var(--cream)}
.brand{position:absolute;left:160px;top:48px;font-size:28px;font-weight:400;color:#4a4a4a;display:flex;align-items:center;gap:10px}
.brand .dot{width:12px;height:12px;border-radius:50%;background:var(--pink-soft)}
.topbar{position:absolute;top:26px;font-size:12px;color:#333;display:flex;align-items:center;gap:6px}
.social{position:absolute;top:23px;display:flex;gap:8px}
.social span{width:20px;height:20px;border-radius:50%;background:var(--pink)}
.search{position:absolute;left:362px;top:98px;width:278px;height:34px;border-radius:17px;background:#fff;font-size:11px;color:var(--pink-soft);padding:10px 20px}
.search svg{position:absolute;right:14px;top:10px}
.nav{position:absolute;top:106px;font-size:13px;color:#333}

/* hero */
.hero{position:absolute;left:0;top:150px;width:1200px;height:604px;background:var(--white)}
.hero-photo{position:absolute;left:470px;top:0;width:730px;height:604px;background:radial-gradient(circle at 60% 40%,#ffffff 0,#f6eef0 30%,#f3b5c8 60%,#e5688f 100%)}
.hero-kicker{position:absolute;left:145px;top:200px;font-size:26px}
.hero-title{position:absolute;left:145px;top:242px;font-size:40px;font-weight:600;line-height:53px}
.btn-sand{position:absolute;left:145px;top:372px;width:140px;height:38px;border-radius:19px;background:var(--sand);font-size:12px;text-align:center;line-height:38px}
.dots{position:absolute;left:578px;top:578px;display:flex;gap:6px}
.dots span{width:10px;height:10px;border-radius:50%;background:var(--pink-soft)}
.dots span:first-child{background:var(--pink)}

/* features */
.features{position:absolute;left:0;top:754px;width:1200px;height:188px;background:var(--cream)}
.feature{position:absolute;top:64px;display:flex;align-items:center;gap:20px}
.icon-circle{width:87px;height:87px;border-radius:50%;background:var(--pink);display:flex;align-items:center;justify-content:center;flex:none}
.feature h3{font-family:"Dancing Script",cursive;font-weight:400;font-size:22px}
.feature p{font-size:11px;color:var(--muted)}

/* arrivals */
.arrivals{position:absolute;left:0;top:942px;width:1200px;height:1262px;background:linear-gradient(var(--cream) 0,var(--cream) 55%,#fbe2e8 100%)}
.section-title{position:absolute;left:0;width:1200px;text-align:center;font-family:"Dancing Script",cursive;font-size:38px}
.section-sub{position:absolute;left:0;width:1200px;text-align:center;font-size:12px}
.product{position:absolute;width:286px;text-align:center}
.product .photo{width:286px;border-radius:10px}
.product h4{font-family:"Dancing Script",cursive;font-weight:400;font-size:21px;margin-top:22px}
.product .price{font-size:15px;font-weight:500;margin-top:6px}
.btn-pink{position:absolute;left:509px;width:182px;height:43px;border-radius:22px;background:var(--pink);color:#fff;font-size:16px;text-align:center;line-height:43px}

/* emotions */
.promise{position:absolute;width:300px;text-align:center}
.promise .icon-circle{margin:0 auto}
.promise h4{font-family:"Dancing Script",cursive;font-weight:400;font-size:21px;margin-top:22px}
.promise p{font-size:12px;line-height:22px;margin-top:4px}
.pill{display:inline-block;margin-top:8px;padding:0 22px;height:24px;line-height:24px;border-radius:12px;background:var(--pink);color:#fff;font-size:11px}

/* sale */
.sale{position:absolute;left:0;top:2656px;width:1200px;height:1385px;background:var(--blush)}
.banner{position:absolute;left:145px;top:79px;width:908px;height:340px;border-radius:14px;background:linear-gradient(110deg,#1e8fb8 0,#4fc0d8 35%,#f3b23e 65%,#e7861d 100%)}
.banner .kicker{position:absolute;left:113px;top:62px;color:#fff;font-size:14px}
.banner .big{position:absolute;left:55px;top:68px;color:#fff;font-family:"Dancing Script",cursive;font-size:80px;line-height:76px}
.banner .btn{position:absolute;left:103px;top:240px;width:116px;height:32px;border-radius:16px;background:#fff;font-size:12px;text-align:center;line-height:32px}

/* florist */
.florist{position:absolute;left:0;top:4041px;width:1200px;height:528px;background:var(--white)}
.florist-photo{position:absolute;left:470px;top:0;width:730px;height:528px;background:radial-gradient(circle at 60% 55%,#f07aa0 0,#f3a9c0 40%,#fbe4ea 75%,#fffefc 100%)}
.benefit{position:absolute;left:145px;display:flex;gap:24px;width:400px}
.benefit .icon-circle{width:68px;height:68px}
.benefit h4{font-family:"Dancing Script",cursive;font-weight:400;font-size:21px}
.benefit p{font-size:11px;line-height:20px;margin-top:2px}

/* footer */
.site-footer{position:absolute;left:0;top:4569px;width:1200px;height:260px;background:var(--cream)}
.footer-col{position:absolute;top:62px;font-size:12px;line-height:26px}
.footer-col h5{font-family:"Dancing Script",cursive;font-weight:400;font-size:20px;line-height:26px;margin-bottom:4px}
.field{width:141px;height:24px;border-radius:12px;background:#fff;font-size:10px;padding:0 14px;line-height:24px;margin-top:8px}
.field-btn{width:80px;height:20px;border-radius:10px;background:var(--pink);color:#fff;font-size:10px;text-align:center;line-height:20px;margin-top:12px}
.round{display:inline-block;width:26px;height:26px;border:1.5px solid #333;border-radius:50%;margin-right:6px;margin-top:6px}
.copyright{position:absolute;left:0;top:4829px;width:1200px;height:24px;background:var(--footer-dark);color:#fff;font-size:10px;text-align:center;line-height:24px}
</style>
</head>
<body>

<header class="site-header">
  <div class="brand"><span class="dot"></span>Petal &amp; Pine</div>
  <div class="topbar" style="left:460px">
    <svg width="12" height="12" viewBox="0 0 24 24"><path d="M6 2l4 4-2 3a12 12 0 006 6l3-2 4 4-3 4C10 21 3 14 2 5z" fill="none" stroke="#f0609e" stroke-width="2"/></svg>555-0142-318
  </div>
  <div class="topbar" style="left:600px">hello@petalandpine.com</div>
  <div class="social" style="left:779px"><span></span><span></span><span></span></div>
  <div class="topbar" style="left:898px">My Account</div>
  <svg class="abs" style="left:993px;top:25px" width="20" height="18" viewBox="0 0 24 22"><path d="M12 21L2 11a5.5 5.5 0 0110-7 5.5 5.5 0 0110 7z" fill="#111"/></svg>
  <svg class="abs" style="left:1030px;top:23px" width="20" height="20" viewBox="0 0 24 24"><path d="M4 8h16l-1 13H5z M8 8a4 4 0 018 0" fill="none" stroke="#111" stroke-width="2"/></svg>
  <div class="search">Search
    <svg width="14" height="14" viewBox="0 0 24 24"><circle cx="10" cy="10" r="7" fill="none" stroke="#f0609e" stroke-width="2.5"/><path d="M15 15l6 6" stroke="#f0609e" stroke-width="2.5"/></svg>
  </div>
  <nav>
    <a class="nav" style="left:674px">Home</a>
    <a class="nav" style="left:759px">Shop ⌄</a>
    <a class="nav" style="left:840px">About</a>
    <a class="nav" style="left:927px">Blog</a>
    <a class="nav" style="left:998px">Contact</a>
  </nav>
</header>

<section class="hero">
  <div class="hero-photo" role="img" aria-label="Bouquet of white lilies and pink roses"></div>
  <p class="hero-kicker script">Let's Fall in Love</p>
  <h1 class="hero-title">Beauty Flowers that<br>Brings happiness</h1>
  <a class="btn-sand">SHOP NOW</a>
  <div class="dots"><span></span><span></span><span></span></div>
</section>

<section class="features">
  <div class="feature" style="left:147px">
    <div class="icon-circle"><svg width="40" height="34" viewBox="0 0 40 34"><rect x="4" y="3" width="32" height="22" rx="2" fill="none" stroke="#fff" stroke-width="2"/><path d="M14 31h12M20 25v6" stroke="#fff" stroke-width="2"/></svg></div>
    <div><h3>Order Online</h3><p>Order bouquet via Online</p></div>
  </div>
  <div class="feature" style="left:477px">
    <div class="icon-circle"><svg width="42" height="30" viewBox="0 0 42 30"><rect x="2" y="4" width="24" height="16" fill="none" stroke="#fff" stroke-width="2"/><path d="M26 9h8l6 6v5H26z" fill="none" stroke="#fff" stroke-width="2"/><circle cx="10" cy="24" r="3" fill="#fff"/><circle cx="32" cy="24" r="3" fill="#fff"/></svg></div>
    <div><h3>Free Shipping</h3><p>For all orders from $100</p></div>
  </div>
  <div class="feature" style="left:786px">
    <div class="icon-circle"><svg width="36" height="36" viewBox="0 0 36 36"><circle cx="18" cy="12" r="6" fill="none" stroke="#fff" stroke-width="2"/><path d="M18 18v14M18 26c-6 0-9-4-9-4M18 24c6 0 9-4 9-4" fill="none" stroke="#fff" stroke-width="2"/></svg></div>
    <div><h3>More Freshness</h3><p>Bouquet are fresh &amp; blooms</p></div>
  </div>
</section>

<section class="arrivals">
  <h2 class="section-title" style="top:72px">Our New Arrivals</h2>
  <p class="section-sub" style="top:130px">A perfect blend of creativity, energy, communication, happiness and love. Let us arrange a smile for you.</p>

  <div class="product" style="left:145px;top:213px"><div class="photo" style="height:373px;background:linear-gradient(160deg,#efe9e4,#e9b8a8 50%,#c9c3b5)" role="img" aria-label="Bride holding a cascading bridal bouquet"></div><h4>Bridal Bouquet</h4><p class="price">$ 200.00</p></div>
  <div class="product" style="left:454px;top:213px"><div class="photo" style="height:373px;background:linear-gradient(160deg,#e9e3e0,#f2a4b6 50%,#c98a96)" role="img" aria-label="Personalized bouquet of pink roses"></div><h4>Personalized Bouquet</h4><p class="price">$ 500.00</p></div>
  <div class="product" style="left:763px;top:213px"><div class="photo" style="height:373px;background:linear-gradient(160deg,#f4f3f3,#f3a6bd 50%,#caa071)" role="img" aria-label="Wicker basket filled with pink gerberas and roses"></div><h4>Basket Bouquet</h4><p class="price">$ 300.00</p></div>

  <div class="product" style="left:145px;top:693px"><div class="photo" style="height:373px;background:linear-gradient(160deg,#8a5a34,#e8e4ee 45%,#8fa3d8 65%,#7a4d2a)" role="img" aria-label="Tussy mussy posy of orchids and hydrangea on wood"></div><h4>Tussy Mussy Bouquet</h4><p class="price">$ 200.00</p></div>
  <div class="product" style="left:454px;top:693px"><div class="photo" style="height:373px;background:linear-gradient(160deg,#5f7a45,#d9b8a6 45%,#c23a4a 75%,#6c8a4a)" role="img" aria-label="Person with flower crown holding red gerbera bouquet"></div><h4>Flower Girl Boutique</h4><p class="price">$ 500.00</p></div>
  <div class="product" style="left:763px;top:693px"><div class="photo" style="height:373px;background:linear-gradient(160deg,#eeeeec,#a33a48 50%,#5f7a64)" role="img" aria-label="Hand-tied bouquet of burgundy roses held in front of a white dress"></div><h4>Hand-Tied Bouquet</h4><p class="price">$ 300.00</p></div>

  <a class="btn-pink" style="top:1183px">Shop More</a>
</section>

<section class="emotions">
  <h2 class="section-title" style="top:2268px">Emotions dressed with lovely flowers</h2>
  <div class="promise" style="left:110px;top:2365px">
    <div class="icon-circle"><svg width="36" height="32" viewBox="0 0 36 32"><path d="M2 3h6l4 18h18l4-13H10" fill="none" stroke="#fff" stroke-width="2.5"/><circle cx="14" cy="27" r="2.5" fill="#fff"/><circle cx="27" cy="27" r="2.5" fill="#fff"/></svg></div>
    <h4>Delivering Your Emotions</h4>
    <p>Send lovely flowers and gifts same<br>day to surprise your loved one</p>
    <a class="pill">Delivery Terms</a>
  </div>
  <div class="promise" style="left:449px;top:2365px">
    <div class="icon-circle"><svg width="40" height="40" viewBox="0 0 40 40"><circle cx="20" cy="20" r="16" fill="none" stroke="#fff" stroke-width="2.5"/><path d="M12 20l6 6 10-12" fill="none" stroke="#fff" stroke-width="3"/></svg></div>
    <h4>100% Fresh Flowers</h4>
    <p>Fresh Flower Basket, Cut Flowers &amp;<br>more at lower price</p>
    <a class="pill">Return Policy</a>
  </div>
  <div class="promise" style="left:786px;top:2365px">
    <div class="icon-circle"><svg width="38" height="38" viewBox="0 0 24 24"><path d="M6 2l4 4-2 3a12 12 0 006 6l3-2 4 4-3 4C10 21 3 14 2 5z" fill="none" stroke="#fff" stroke-width="1.6"/></svg></div>
    <h4>Online Flowers Delivery</h4>
    <p>24/7 Flower &amp; Bouquet delivery with<br>hassle free support</p>
    <a class="pill">Support Terms</a>
  </div>
</section>

<section class="sale">
  <div class="banner" role="img" aria-label="Orange poppies against a blue sky">
    <p class="kicker">Take Upto 50% Off</p>
    <p class="big">Spring<br>&nbsp;&nbsp;&nbsp;&nbsp;Sale</p>
    <a class="btn">Shop Now</a>
  </div>

  <div class="product" style="left:145px;top:468px"><div class="photo" style="height:320px;background:linear-gradient(160deg,#eef0f0,#f0a7bd 50%,#dfe3e2)" role="img" aria-label="Pink roses with baby's breath"></div><h4>Tussy Mussy Bouquet</h4><p class="price">$ 200.00</p></div>
  <div class="product" style="left:454px;top:468px"><div class="photo" style="height:320px;background:linear-gradient(160deg,#4c6b3a,#d8b9a3 40%,#f0cf2a 70%,#5b7a3a)" role="img" aria-label="Person holding yellow wildflowers"></div><h4>Flower Girl Boutique</h4><p class="price">$ 500.00</p></div>
  <div class="product" style="left:763px;top:468px"><div class="photo" style="height:320px;background:linear-gradient(160deg,#6b5a4a,#d9b7b6 45%,#9aa77e)" role="img" aria-label="Antique pink roses and greenery"></div><h4>Hand-Tied Bouquet</h4><p class="price">$ 300.00</p></div>

  <div class="product" style="left:145px;top:899px"><div class="photo" style="height:320px;background:linear-gradient(160deg,#6a4a3a,#f0c6cc 45%,#b84f86)" role="img" aria-label="Peony and tulip bouquet"></div><h4>Tussy Mussy Bouquet</h4><p class="price">$ 200.00</p></div>
  <div class="product" style="left:454px;top:899px"><div class="photo" style="height:320px;background:linear-gradient(160deg,#2f5a2a,#d0222e 50%,#8c1a22)" role="img" aria-label="Person among red roses"></div><h4>Flower Girl Boutique</h4><p class="price">$ 500.00</p></div>
  <div class="product" style="left:763px;top:899px"><div class="photo" style="height:320px;background:linear-gradient(160deg,#4a3a2e,#e8642c 45%,#5a7a8a)" role="img" aria-label="Orange roses and thistles in a hand-tied bouquet"></div><h4>Hand-Tied Bouquet</h4><p class="price">$ 300.00</p></div>
</section>

<section class="florist">
  <div class="florist-photo" role="img" aria-label="Pile of pink roses"></div>
  <h2 class="abs script" style="left:145px;top:72px;font-size:32px">The Florist – to fulfill your bouquet needs</h2>
  <div class="benefit" style="top:166px">
    <div class="icon-circle"><svg width="34" height="34" viewBox="0 0 34 34"><circle cx="17" cy="17" r="14" fill="none" stroke="#fff" stroke-width="2"/><text x="17" y="21" fill="#fff" font-size="10" font-family="Poppins,sans-serif" text-anchor="middle">24h</text></svg></div>
    <div><h4>Adorning Life Moments</h4><p>Vitae et leo duis ut diam quam. Aliquam vesti-<br>bulum morbi blandit.</p></div>
  </div>
  <div class="benefit" style="top:280px">
    <div class="icon-circle"><svg width="34" height="34" viewBox="0 0 34 34"><circle cx="17" cy="17" r="14" fill="none" stroke="#fff" stroke-width="2"/><path d="M10 17l5 5 9-10" fill="none" stroke="#fff" stroke-width="2.5"/></svg></div>
    <div><h4>100% Freshness Guaranteed</h4><p>Turpis egestas pretium aenean pharetra<br>magna ac placerat.</p></div>
  </div>
  <div class="benefit" style="top:394px">
    <div class="icon-circle"><svg width="32" height="28" viewBox="0 0 36 32"><path d="M2 3h6l4 18h18l4-13H10" fill="none" stroke="#fff" stroke-width="2.5"/><circle cx="14" cy="27" r="2.5" fill="#fff"/><circle cx="27" cy="27" r="2.5" fill="#fff"/></svg></div>
    <div><h4>Delivering Smiles Daily!</h4><p>Aliquam id diam maecenas ultricies mi eget<br>mauris pharetra et.</p></div>
  </div>
</section>

<footer class="site-footer">
  <div class="brand" style="left:145px;top:100px;font-size:30px"><span class="dot"></span>Petal &amp; Pine</div>
  <div class="footer-col" style="left:384px"><h5>Navigation</h5>Home<br>Shop<br>About<br>Blog<br>Contact</div>
  <div class="footer-col" style="left:527px"><h5>Help</h5>Search<br>Help<br>Information<br>Privacy Policy<br>Shipping Details</div>
  <div class="footer-col" style="left:697px"><h5>Contact Us</h5>Phone: 555-0142-318<br>Fax: 555-0142-318<br>hello@petalandpine.com<br><span class="round"></span><span class="round"></span><span class="round"></span></div>
  <div class="footer-col" style="left:910px"><h5>Subscribe</h5><div class="field">Name</div><div class="field">Email</div><div class="field-btn">Subscribe</div></div>
</footer>
<div class="copyright">Copyright © Petal &amp; Pine 2021. All rights reserved</div>

</body>
</html>
```